pharmacy/travel clinic business card design

We need a business card for our new business called Brenwick Travel Clinic and Pharmacy. Our primary focus is doing consultations for people before travelling internationally and providing vaccinations and prescriptions for them. While the business is considered a pharmacy, it has more the look and feel of a doctor's office. The design should communicate a professional and trustworthy feel. I have attached a copy of the logo we are going to be using.
Updates
Thanks for the submissions.  If you haven`t been eliminated you are one of the finalists.  Decision will likely be made tomorrow.

Target Market(s)
Customers, other health care professionals, travel agents
Industry/Entity Type
Clinic
Look and feel
Each slider illustrates characteristics of the customer's brand and the style your logo design should communicate.

```html
<!DOCTYPE html>
<html lang="en">
<head>
<meta charset="utf-8">
<title>Brenwick Travel Clinic and Pharmacy — Business Cards</title>
<link rel="stylesheet" href="https://fonts.googleapis.com/css2?family=Montserrat:wght@400;500;600&display=swap">
<style>
  :root {
    --bg-top: #8f8f8f;
    --bg-bottom: #f2f2f2;
    --green-deep: #7dbd35;
    --green-light: #b4da7c;
    --blue-deep: #1f3586;
    --blue-mid: #2a6fb8;
    --blue-light: #62c0ea;
    --ink: #ffffff;
    --ink-soft: rgba(255, 255, 255, 0.85);
  }
  * { margin: 0; padding: 0; box-sizing: border-box; }
  html, body { width: 1200px; height: 861px; overflow: hidden; }
  body {
    background: linear-gradient(180deg, var(--bg-top) 0%, var(--bg-bottom) 85%);
    font-family: "Montserrat", Arial, sans-serif;
    color: var(--ink);
    display: flex;
    justify-content: center;
    align-items: center;
    gap: 100px;
  }
  .business-card {
    position: relative;
    width: 300px;
    height: 520px;
    border-radius: 22px;
    padding: 34px 28px 32px;
    display: flex;
    flex-direction: column;
    box-shadow: 0 10px 24px rgba(0, 0, 0, 0.25);
  }
  .business-card--green {
    background: linear-gradient(200deg, var(--green-light) 0%, var(--green-deep) 75%);
  }
  .business-card--blue {
    background: linear-gradient(200deg, var(--blue-light) 0%, var(--blue-mid) 40%, var(--blue-deep) 85%);
  }
  .brand {
    display: flex;
    align-items: flex-start;
    gap: 10px;
  }
  .brand__dot {
    width: 12px;
    height: 12px;
    border-radius: 50%;
    background: var(--ink);
    margin-top: 5px;
    flex: none;
  }
  .brand__name {
    font-size: 18px;
    font-weight: 600;
    line-height: 1.25;
    color: var(--ink);
    max-width: 200px;
  }
  .holder {
    margin-top: 34px;
    text-align: right;
  }
  .holder__name {
    font-size: 19px;
    font-weight: 500;
    letter-spacing: 0.8px;
  }
  .holder__position {
    font-size: 12px;
    margin-top: 4px;
    color: var(--ink-soft);
  }
  .contacts {
    margin-top: auto;
    list-style: none;
    font-size: 10px;
    color: var(--ink-soft);
  }
  .contacts__item {
    display: flex;
    align-items: center;
    gap: 9px;
    margin-top: 7px;
  }
  .contacts__icon {
    width: 12px;
    height: 12px;
    flex: none;
  }
</style>
</head>
<body>

  <article class="business-card business-card--green">
    <header class="brand">
      <span class="brand__dot"></span>
      <p class="brand__name">Brenwick Travel Clinic and Pharmacy</p>
    </header>
    <section class="holder">
      <h2 class="holder__name">NAME SURNAME</h2>
      <p class="holder__position">Position</p>
    </section>
    <ul class="contacts">
      <li class="contacts__item"><svg class="contacts__icon" viewBox="0 0 12 12"><circle cx="6" cy="6" r="6" fill="#fff"/><path d="M6 2.5a2.2 2.2 0 0 0-2.2 2.2C3.8 6.4 6 9.5 6 9.5s2.2-3.1 2.2-4.8A2.2 2.2 0 0 0 6 2.5z" fill="#7dbd35"/></svg>123 Lorem Ipsum St. Dolor Sit City 1234</li>
      <li class="contacts__item"><svg class="contacts__icon" viewBox="0 0 12 12"><circle cx="6" cy="6" r="6" fill="#fff"/><path d="M4 3l1.2 1.5-.6.8a4 4 0 0 0 2.1 2.1l.8-.6L9 8 8.2 9C5.5 8.8 3.2 6.5 3 3.8z" fill="#7dbd35"/></svg>123.456.7890</li>
      <li class="contacts__item"><svg class="contacts__icon" viewBox="0 0 12 12"><circle cx="6" cy="6" r="6" fill="#fff"/><rect x="3" y="4" width="6" height="4.5" fill="#7dbd35"/></svg>098.765.4321</li>
      <li class="contacts__item"><svg class="contacts__icon" viewBox="0 0 12 12"><circle cx="6" cy="6" r="6" fill="#fff"/><path d="M2.8 4h6.4v4.2H2.8zM2.8 4 6 6.5 9.2 4" fill="none" stroke="#7dbd35" stroke-width="0.9"/></svg>name@brenwicktcp.com</li>
      <li class="contacts__item"><svg class="contacts__icon" viewBox="0 0 12 12"><circle cx="6" cy="6" r="6" fill="#fff"/></svg>brenwicktcp</li>
      <li class="contacts__item"><svg class="contacts__icon" viewBox="0 0 12 12"><circle cx="6" cy="6" r="6" fill="#fff"/></svg>brenwicktcp</li>
      <li class="contacts__item"><svg class="contacts__icon" viewBox="0 0 12 12"><circle cx="6" cy="6" r="6" fill="#fff"/><circle cx="6" cy="6" r="3" fill="none" stroke="#7dbd35" stroke-width="0.9"/><path d="M3 6h6M6 3v6" stroke="#7dbd35" stroke-width="0.7"/></svg>www.brenwicktcp.com</li>
    </ul>
  </article>

  <article class="business-card business-card--blue">
    <header class="brand">
      <span class="brand__dot"></span>
      <p class="brand__name">Brenwick Travel Clinic and Pharmacy</p>
    </header>
    <section class="holder">
      <h2 class="holder__name">NAME SURNAME</h2>
      <p class="holder__position">Position</p>
    </section>
    <ul class="contacts">
      <li class="contacts__item"><svg class="contacts__icon" viewBox="0 0 12 12"><circle cx="6" cy="6" r="6" fill="#fff"/><path d="M6 2.5a2.2 2.2 0 0 0-2.2 2.2C3.8 6.4 6 9.5 6 9.5s2.2-3.1 2.2-4.8A2.2 2.2 0 0 0 6 2.5z" fill="#1f3586"/></svg>123 Lorem Ipsum St. Dolor Sit City 1234</li>
      <li class="contacts__item"><svg class="contacts__icon" viewBox="0 0 12 12"><circle cx="6" cy="6" r="6" fill="#fff"/><path d="M4 3l1.2 1.5-.6.8a4 4 0 0 0 2.1 2.1l.8-.6L9 8 8.2 9C5.5 8.8 3.2 6.5 3 3.8z" fill="#1f3586"/></svg>123.456.7890</li>
      <li class="contacts__item"><svg class="contacts__icon" viewBox="0 0 12 12"><circle cx="6" cy="6" r="6" fill="#fff"/><rect x="3" y="4" width="6" height="4.5" fill="#1f3586"/></svg>098.765.4321</li>
      <li class="contacts__item"><svg class="contacts__icon" viewBox="0 0 12 12"><circle cx="6" cy="6" r="6" fill="#fff"/><path d="M2.8 4h6.4v4.2H2.8zM2.8 4 6 6.5 9.2 4" fill="none" stroke="#1f3586" stroke-width="0.9"/></svg>name@brenwicktcp.com</li>
      <li class="contacts__item"><svg class="contacts__icon" viewBox="0 0 12 12"><circle cx="6" cy="6" r="6" fill="#fff"/></svg>brenwicktcp</li>
      <li class="contacts__item"><svg class="contacts__icon" viewBox="0 0 12 12"><circle cx="6" cy="6" r="6" fill="#fff"/></svg>brenwicktcp</li>
      <li class="contacts__item"><svg class="contacts__icon" viewBox="0 0 12 12"><circle cx="6" cy="6" r="6" fill="#fff"/><circle cx="6" cy="6" r="3" fill="none" stroke="#1f3586" stroke-width="0.9"/><path d="M3 6h6M6 3v6" stroke="#1f3586" stroke-width="0.7"/></svg>www.brenwicktcp.com</li>
    </ul>
  </article>

</body>
</html>
```